New Toothpaste brand needs a logo & packaging design

Our company is launching a new toothpaste and is looking for a logo and packaging design. The toothpaste brand is called Brivana. The packaging should have the same design quality as the major international brands, such as Lumora, Lumora Totalcare, Dentiva, Pexolo, Wind-rise, Marvest, etc. The dominant colors for our brand should be hues of blue, similar to other major brands. In addition, there should be a little bit of green to represent the "Fresh Mint Blast" flavor and the "Extracts of Aloe Vera" included in the ingredients.

There are typically 3 unique sides on a toothpaste box:

The face: Repeated on ~3 sides of the 4 faces of the box
The back: The 4th box face has the instructions for use, ingredients, company information, bar code/product info, and some branding elements.
The sides: Usually consisting of just the logo, flavor etc.

Please refer to existing brands such as Lumora, Lumora Total-care, and Dentiva for an example of typical box layout and elements.

Task Details:
Package Dimensions: 180 mm x 48 mm x 28 mm, 100 ml toothpaste tube
Brand Name: Brivana
Description: Fluoride Toothpaste
Flavor: Fresh Mint Blast
5 Actions: Protects against cavities and tartar, freshens breath, whitens teeth, and maintains healthy gums. These actions can also be made into a list like Lumora Total Care or Dentiva Max care. For instance, Strong Teeth, Fresh Breath, Whitening, Healthy Gums, Cavity and Tartar Protection.
Also contains whitening micro particles and extracts of aloe vera which may be highlighted on the package

Overall, the look should be high quality and with the same look and feel as the big brands mentioned previously. We do not have an existing logo for this brand. The face of the package is the most important element as it is often repeated on several sides and on the tube itself.

Please let me know if you have any questions.

I've attached some of our favorite big brand designs below. I would say the Lumora Total Care and Gleam vers

The logos I've seen so far for Brivana, have been a bit too bold. A little bold is okay, but just needs to be moderate. 

I would like the colors to be bright and appealing. I mentioned shades of blue being the major color, but green should also be highlighted as well, perhaps in a 80% blue to 20% green ratio. 

Target Market(s)

adult consumer of toothpaste, both female and male.

Industry/Entity Type

It Company

Requirements
Must have
• A logo with the brand name: Brivana
Description or sub text: Fluoride Toothpaste
Flavor: Fresh Mint Blast
A phrase or list describing the Toothpaste Actions: e.g., Protects against cavities and tartar, freshens breath, whitens teeth, and maintains healthy gums. Or as a list simialr to Lumora Total Care or Dentiva Max Care:
-Anti-cavity
-Anti-tartar
-Fresh breath
-Whitening
-Healthy Gums

Special ingredient of "whitening micro particles: and "extracts of aloe vera", which should also be highlighted.

The color should mostly be shades of blue, with only a little bit of green to accentuate the fresh mint blast flavor and aloe vera

Nice to have
• The design should really look good next to lumora total care, gleam pure, and dentiva max care. These are our favorite designs.
Should not have
• For aloe vera, there is no need to show the plant.

The Brivana logo shouldn't be too Bold. This should be appeal to all consumers, not just men.

```html
<!DOCTYPE html>
<html lang="en">
<head>
<meta charset="utf-8">
<title>Brivana Fluoride Toothpaste – Box Dieline</title>
<link rel="stylesheet" href="https://fonts.googleapis.com/css2?family=PT+Sans:ital,wght@0,400;0,700;1,700&display=swap">
<style>
  :root{
    --paper:#ffffff;
    --line:#1a1a1a;
    --aqua-deep:#8eeff5;
    --aqua-bright:#3ae8f2;
    --aqua-mid:#86eef4;
    --aqua-soft:#b6f6f9;
    --aqua-pale:#d8fcfd;
    --brand-blue:#1768c9;
    --text-blue:#1f5fc0;
    --ink:#23406b;
    --mint-green:#38c21c;
    --leaf-green:#5fcf3c;
    --leaf-dark:#2e8a1c;
  }
  *{margin:0;padding:0;box-sizing:border-box}
  html,body{width:1200px;height:779px;overflow:hidden;background:var(--paper)}
  body{position:relative;font-family:"PT Sans",Arial,sans-serif}

  .dieline{position:absolute;inset:0}
  .panel{position:absolute;border:1.5px solid var(--line);overflow:hidden;background:var(--paper)}
  .back-panel{left:150px;top:12px;width:892px;height:238px}
  .face{left:150px;width:892px}
  .face--upper{top:249px;height:138px}
  .face--main{top:386px;height:241px}
  .face--lower{top:626px;height:145px}
  .end-flap{top:386px;height:241px}
  .end-flap--left{left:12px;width:139px}
  .end-flap--right{left:1041px;width:141px}

  .face-bg{position:absolute;inset:0;width:100%;height:100%}

  .brand-mark{position:absolute;background:var(--brand-blue)}
  .brand-name{position:absolute;color:var(--brand-blue);font-weight:700;font-size:56px;line-height:1;letter-spacing:1px;white-space:nowrap}
  .descriptor{position:absolute;color:var(--text-blue);font-style:italic;font-weight:700;font-size:19px;line-height:1;white-space:nowrap}
  .flavor{position:absolute;color:var(--mint-green);font-style:italic;font-weight:700;font-size:27px;line-height:1.05;transform:rotate(-6deg);transform-origin:left top;white-space:nowrap}
  .flavor span{display:block}
  .mint-leaves{position:absolute;border-radius:50% 50% 45% 45%;background:radial-gradient(circle at 50% 45%,var(--leaf-green),var(--leaf-dark))}
  .benefits{position:absolute;list-style:none;color:var(--text-blue);font-style:italic;font-weight:700;font-size:14.5px;line-height:1.22}
  .benefits li{padding-left:11px;position:relative;white-space:nowrap}
  .benefits li::before{content:"•";position:absolute;left:0}

  /* upper face */
  .face--upper .brand-mark{left:52px;top:16px;width:104px;height:104px}
  .face--upper .brand-name{left:190px;top:26px}
  .face--upper .descriptor{left:214px;top:86px}
  .face--upper .flavor{left:478px;top:22px}
  .face--upper .mint-leaves{left:566px;top:52px;width:80px;height:62px}
  .face--upper .benefits{left:683px;top:20px}

  /* main face */
  .face--main .brand-mark{left:20px;top:50px;width:126px;height:126px}
  .face--main .brand-name{left:190px;top:78px}
  .face--main .descriptor{left:214px;top:138px}
  .face--main .flavor{left:442px;top:76px}
  .face--main .mint-leaves{left:534px;top:112px;width:92px;height:72px}
  .face--main .benefits{left:683px;top:72px}

  /* lower face */
  .face--lower .brand-mark{left:52px;top:18px;width:106px;height:106px}
  .face--lower .brand-name{left:190px;top:30px}
  .face--lower .descriptor{left:214px;top:90px}
  .face--lower .flavor{left:478px;top:26px}
  .face--lower .mint-leaves{left:566px;top:58px;width:80px;height:62px}
  .face--lower .benefits{left:683px;top:22px}

  /* end flaps */
  .end-logo{position:absolute;left:50%;top:50%;width:200px;height:70px;transform:translate(-50%,-50%) rotate(-90deg)}
  .end-logo .brand-mark{left:0;top:8px;width:54px;height:54px}
  .end-logo .brand-name{left:64px;top:6px;font-size:34px}
  .end-logo .descriptor{left:66px;top:44px;font-size:12px}

  /* back panel */
  .back-panel{padding:18px 28px;display:grid;grid-template-columns:1.1fr 1.3fr 1fr;gap:26px;color:var(--ink)}
  .back-heading{font-weight:700;font-size:14px;color:var(--brand-blue);text-transform:uppercase;letter-spacing:.5px;margin-bottom:6px}
  .back-copy{font-size:12.5px;line-height:1.4}
  .back-brand{font-weight:700;font-size:30px;color:var(--brand-blue);line-height:1}
  .back-descriptor{font-style:italic;font-weight:700;font-size:14px;color:var(--text-blue);margin:4px 0 12px}
  .ingredient-highlights{list-style:none;display:flex;flex-direction:column;gap:6px;margin-top:10px}
  .highlight{display:flex;align-items:center;gap:8px;font-weight:700;font-size:13px;padding:6px 10px;border-radius:16px;white-space:nowrap}
  .highlight::before{content:"";width:10px;height:10px;border-radius:50%;flex:none}
  .highlight--whitening{background:var(--aqua-pale);color:var(--brand-blue)}
  .highlight--whitening::before{background:var(--aqua-bright)}
  .highlight--aloe{background:#e6f8df;color:var(--leaf-dark)}
  .highlight--aloe::before{background:var(--mint-green)}
  .net-content{margin-top:12px;font-weight:700;font-size:13px;color:var(--brand-blue)}
</style>
</head>
<body>
<main class="dieline">

  <section class="panel back-panel" aria-label="Back panel">
    <div class="back-column">
      <p class="back-brand">Brivana</p>
      <p class="back-descriptor">Fluoride Toothpaste · Fresh Mint Blast</p>
      <ul class="ingredient-highlights">
        <li class="highlight highlight--whitening">With whitening micro particles</li>
        <li class="highlight highlight--aloe">With extracts of aloe vera</li>
      </ul>
    </div>
    <div class="back-column">
      <h2 class="back-heading">Directions</h2>
      <p class="back-copy">Adults and children over 6: brush teeth thoroughly at least twice a day, or as directed by a dentist. Do not swallow. Children under 6: use a pea-sized amount under adult supervision.</p>
      <h2 class="back-heading" style="margin-top:10px">Ingredients</h2>
      <p class="back-copy">Sodium fluoride 0.24%, sorbitol, water, hydrated silica, whitening micro particles, aloe vera leaf extract, flavour, cellulose gum.</p>
    </div>
    <div class="back-column">
      <h2 class="back-heading">Actions</h2>
      <p class="back-copy">Anti-cavity · Anti-tartar<br>Fresh breath · Whitening<br>Healthy gums</p>
      <h2 class="back-heading" style="margin-top:10px">Made by</h2>
      <p class="back-copy">Brivana Oral Care</p>
      <p class="net-content">100 ml</p>
    </div>
  </section>

  <section class="panel face face--upper">
    <svg class="face-bg" viewBox="0 0 100 100" preserveAspectRatio="none" aria-hidden="true">
      <rect width="100" height="100" fill="var(--aqua-pale)"/>
      <polygon points="0,0 58,0 64,50 58,100 0,100" fill="var(--aqua-soft)"/>
      <polygon points="0,0 43,0 49,50 43,100 0,100" fill="var(--aqua-mid)"/>
      <polygon points="0,0 33,0 39,50 33,100 0,100" fill="var(--aqua-bright)"/>
      <polygon points="0,0 24,0 30,50 24,100 0,100" fill="var(--aqua-deep)"/>
    </svg>
    <span class="brand-mark" aria-hidden="true"></span>
    <span class="brand-name">Brivana</span>
    <span class="descriptor">Fluoride Toothpaste</span>
    <p class="flavor"><span>Fresh Mint</span><span>Blast</span></p>
    <div class="mint-leaves" role="img" aria-label="Illustration of fresh mint leaves"></div>
    <ul class="benefits">
      <li>Protect against cavity<br>and tartar</li>
      <li>Freshens breath</li>
      <li>Whitens teeth</li>
      <li>Maintains healthy gums</li>
    </ul>
  </section>

  <section class="panel end-flap end-flap--left">
    <div class="end-logo">
      <span class="brand-mark" aria-hidden="true"></span>
      <span class="brand-name">Brivana</span>
      <span class="descriptor">Fluoride Toothpaste</span>
    </div>
  </section>

  <section class="panel face face--main">
    <svg class="face-bg" viewBox="0 0 100 100" preserveAspectRatio="none" aria-hidden="true">
      <rect width="100" height="100" fill="var(--aqua-pale)"/>
      <polygon points="0,0 58,0 64,50 58,100 0,100" fill="var(--aqua-soft)"/>
      <polygon points="0,0 43,0 49,50 43,100 0,100" fill="var(--aqua-mid)"/>
      <polygon points="0,0 33,0 39,50 33,100 0,100" fill="var(--aqua-bright)"/>
      <polygon points="0,0 24,0 30,50 24,100 0,100" fill="var(--aqua-deep)"/>
    </svg>
    <span class="brand-mark" aria-hidden="true"></span>
    <span class="brand-name">Brivana</span>
    <span class="descriptor">Fluoride Toothpaste</span>
    <p class="flavor"><span>Fresh Mint</span><span>Blast</span></p>
    <div class="mint-leaves" role="img" aria-label="Illustration of fresh mint leaves"></div>
    <ul class="benefits">
      <li>Protect against cavity<br>and tartar</li>
      <li>Freshens breath</li>
      <li>Whitens teeth</li>
      <li>Maintains healthy gums</li>
    </ul>
  </section>

  <section class="panel end-flap end-flap--right">
    <div class="end-logo">
      <span class="brand-mark" aria-hidden="true"></span>
      <span class="brand-name">Brivana</span>
      <span class="descriptor">Fluoride Toothpaste</span>
    </div>
  </section>

  <section class="panel face face--lower">
    <svg class="face-bg" viewBox="0 0 100 100" preserveAspectRatio="none" aria-hidden="true">
      <rect width="100" height="100" fill="var(--aqua-pale)"/>
      <polygon points="0,0 58,0 64,50 58,100 0,100" fill="var(--aqua-soft)"/>
      <polygon points="0,0 43,0 49,50 43,100 0,100" fill="var(--aqua-mid)"/>
      <polygon points="0,0 33,0 39,50 33,100 0,100" fill="var(--aqua-bright)"/>
      <polygon points="0,0 24,0 30,50 24,100 0,100" fill="var(--aqua-deep)"/>
    </svg>
    <span class="brand-mark" aria-hidden="true"></span>
    <span class="brand-name">Brivana</span>
    <span class="descriptor">Fluoride Toothpaste</span>
    <p class="flavor"><span>Fresh Mint</span><span>Blast</span></p>
    <div class="mint-leaves" role="img" aria-label="Illustration of fresh mint leaves"></div>
    <ul class="benefits">
      <li>Protect against cavity<br>and tartar</li>
      <li>Freshens breath</li>
      <li>Whitens teeth</li>
      <li>Maintains healthy gums</li>
    </ul>
  </section>

</main>
</body>
</html>
```